DL Flyer showing product benefits

We sell massage chairs and need a DL size double sided flyer describing the benefits of our products. This will be handed out to customers in our stores. Please use the content shown on the attached flyer. On the back will be our logo, phone number and web address (1300 482 736, velmorarecliners.com.au). I have attached our brand guidelines for reference.

Target Market(s)

35-55, men and women

Colors

Designer to choose colors to be used in the design.

Requirements
Must have
• Content provided
• Logo
• Company branding
• Contact details

```html
<!DOCTYPE html>
<html lang="en">
<head>
<meta charset="utf-8">
<title>Velmora DL Flyer</title>
<link rel="stylesheet" href="https://fonts.googleapis.com/css2?family=Josefin+Sans:wght@400;600;700&display=swap">
<style>
  :root {
    --navy: #17242c;
    --orange: #f47c16;
    --amber: #f9a51a;
    --yellow: #fbc02d;
    --paper: #f7f7f6;
    --ink: #141c21;
    --bg: #e9e6e1;
    --chair: #4a3a30;
    --ghost: #e6e6e6;
  }
  * { box-sizing: border-box; margin: 0; padding: 0; }
  html, body { width: 1200px; height: 900px; overflow: hidden; }
  body {
    background: var(--bg);
    font-family: "Josefin Sans", "Helvetica Neue", Arial, sans-serif;
    color: var(--ink);
    position: relative;
  }
  .flyer {
    position: absolute;
    top: 30px;
    width: 400px;
    height: 840px;
    background: var(--paper);
    overflow: hidden;
    box-shadow: 0 6px 18px rgba(0,0,0,.18);
  }
  .flyer--front { left: 170px; }
  .flyer--back { left: 630px; }
  .flyer__shapes { position: absolute; inset: 0; width: 100%; height: 100%; }

  .brand {
    position: absolute;
    display: flex;
    align-items: center;
    gap: 10px;
    color: #fff;
    font-weight: 600;
    font-size: 26px;
    letter-spacing: 2px;
  }
  .brand__dot { width: 14px; height: 14px; border-radius: 50%; background: #fff; }
  .flyer--front .brand { top: 48px; right: 36px; }
  .flyer--back .brand { top: 52px; left: 28px; font-size: 22px; }

  .headline {
    position: absolute;
    font-weight: 700;
    line-height: 1.1;
    color: var(--ink);
    white-space: nowrap;
  }
  .flyer--front .headline { top: 290px; left: 36px; font-size: 34px; }
  .flyer--back .headline {
    top: 130px; left: 128px; width: 256px;
    font-size: 24px; text-align: center;
  }

  .product-photo {
    position: absolute;
    left: 70px; top: 410px;
    width: 290px; height: 210px;
    border-radius: 40px 70px 20px 30px;
    background: linear-gradient(135deg, #6b5444, var(--chair) 55%, #2a211c);
  }
  .product-ghost {
    position: absolute;
    left: 210px; top: 230px;
    width: 160px; height: 350px;
    border-radius: 60px 40px 30px 50px;
    background: linear-gradient(180deg, var(--ghost), #efefef);
  }

  .contact {
    position: absolute;
    left: 0; right: 0; bottom: 36px;
    text-align: center;
    color: #fff;
  }
  .contact__phone { font-size: 28px; font-weight: 700; letter-spacing: 1px; }
  .contact__web { font-size: 15px; margin-top: 6px; letter-spacing: .5px; }

  .benefits {
    position: absolute;
    left: 40px; top: 250px;
    list-style: none;
  }
  .benefits li {
    display: flex;
    align-items: center;
    gap: 14px;
    height: 38px;
    font-size: 15px;
    font-weight: 600;
    white-space: nowrap;
  }
  .benefits svg { width: 30px; height: 30px; flex: none; }
</style>
</head>
<body>

<section class="flyer flyer--front">
  <svg class="flyer__shapes" viewBox="0 0 400 840" aria-hidden="true">
    <path d="M0 0H400V235C300 170 170 130 0 125Z" fill="var(--navy)"/>
    <path d="M0 125C120 125 220 150 290 185L0 275Z" fill="var(--orange)"/>
    <path d="M0 700C130 650 260 640 400 590V840H0Z" fill="var(--yellow)"/>
    <path d="M0 715C140 690 260 660 400 620V840H0Z" fill="var(--orange)"/>
    <path d="M0 740C150 720 280 700 400 660V840H0Z" fill="var(--navy)"/>
  </svg>
  <div class="brand"><span class="brand__dot"></span>Velmora</div>
  <h1 class="headline">Get in touch and feel<br>the difference</h1>
  <div class="product-photo" role="img" aria-label="Photo of a brown reclining massage chair"></div>
  <div class="contact">
    <p class="contact__phone">1300 482 736</p>
    <p class="contact__web">www.velmorarecliners.com.au</p>
  </div>
</section>

<section class="flyer flyer--back">
  <svg class="flyer__shapes" viewBox="0 0 400 840" aria-hidden="true">
    <path d="M0 0H255C170 40 110 120 92 228L0 236Z" fill="var(--navy)"/>
    <path d="M255 0H400V150C350 110 300 60 255 0Z" fill="var(--orange)"/>
    <path d="M0 710C130 670 260 650 400 600V840H0Z" fill="var(--yellow)"/>
    <path d="M0 730C140 700 260 675 400 635V840H0Z" fill="var(--orange)"/>
    <path d="M0 755C150 735 280 715 400 675V840H0Z" fill="var(--navy)"/>
  </svg>
  <div class="brand"><span class="brand__dot"></span>Velmora</div>
  <div class="product-ghost" role="img" aria-label="Faint background photo of a massage chair"></div>
  <h2 class="headline">Get in touch and feel<br>the difference</h2>
  <ul class="benefits">
    <li><svg viewBox="0 0 30 30"><circle cx="15" cy="15" r="15" fill="var(--navy)"/><path d="M9 17q6 6 12 0" stroke="#fff" stroke-width="2" fill="none"/></svg>Relax &amp; Reduce stress</li>
    <li><svg viewBox="0 0 30 30"><circle cx="15" cy="15" r="15" fill="var(--navy)"/><path d="M9 10l12 10M21 10L9 20" stroke="#fff" stroke-width="2.5"/></svg>Ease Joint Pain</li>
    <li><svg viewBox="0 0 30 30"><circle cx="15" cy="15" r="15" fill="var(--navy)"/><rect x="7" y="11" width="15" height="8" fill="none" stroke="#fff" stroke-width="1.8"/><rect x="22" y="13.5" width="2" height="3" fill="#fff"/><rect x="9" y="13" width="9" height="4" fill="#fff"/></svg>Increase Energy</li>
    <li><svg viewBox="0 0 30 30"><circle cx="15" cy="15" r="15" fill="var(--navy)"/><path d="M8 22L22 8M10 12q6 0 10 8" stroke="#fff" stroke-width="2" fill="none"/></svg>Improve Circulation</li>
    <li><svg viewBox="0 0 30 30"><circle cx="15" cy="15" r="15" fill="var(--navy)"/><rect x="7" y="15" width="16" height="5" rx="2" fill="#fff"/><circle cx="11" cy="12" r="2.5" fill="#fff"/></svg>Improve Sleep</li>
    <li><svg viewBox="0 0 30 30"><circle cx="15" cy="15" r="15" fill="var(--navy)"/><path d="M15 7l7 3v5q0 6-7 9q-7-3-7-9v-5z" fill="#fff"/></svg>Boost Immunity</li>
    <li><svg viewBox="0 0 30 30"><circle cx="15" cy="15" r="15" fill="var(--navy)"/><path d="M15 7v16M11 12l4-3 4 3" stroke="#fff" stroke-width="2" fill="none"/></svg>Relieve Muscle Tension</li>
    <li><svg viewBox="0 0 30 30"><circle cx="15" cy="15" r="15" fill="var(--navy)"/><path d="M8 18q3-8 7-4t7-4" stroke="#fff" stroke-width="3" fill="none"/></svg>Enhance Fitness</li>
    <li><svg viewBox="0 0 30 30"><circle cx="15" cy="15" r="15" fill="var(--navy)"/><path d="M15 22l-6-6a3.5 3.5 0 0 1 6-4a3.5 3.5 0 0 1 6 4z" fill="none" stroke="#fff" stroke-width="1.8"/></svg>Improve Health</li>
  </ul>
</section>

</body>
</html>
```